Design a few pages of a luxury magazine for the Prestige Aubergerie Lyon

We need a luxury design for our magazine. See the inDesign pages of the current version attached (zip).

Please work primarily on the first double page (Inventez le luxe de demain) that contains only one photo with legend, a title and the text both in French and English. It must be made clear that the text is the same in two different languages (it is not clear enough here).

You can also work on the other two double pages selected. Feedback will be provided and the 10 best pages will be submitted to a vote at the end of the project timespan.

The most important is a classy and luxury design, this will be printed on expensive paper.

See the full brochure here: https://www.prestigeaubergerie.com/brochure/#page=4

Target Market(s)

Students and parents

Industry/Entity Type

Education

Colors

Designer to choose colors to be used in the design.

Requirements
Must have
• Luxury magazine layout, see:
• https://www.findwerk.com/search?q=luxury+magazine+layout&client=safari&rls=en&source=lnms&tbm=isch&sa=X&ved=0ahUKEwitoIDmit7fAhUVShUIHXC2Cd4Q_AUIDigB&biw=1010&bih=702
Nice to have
• The color of the cover that should be used for blue and grey is #393d49.
• Our font for serif titles (from the logo) is Adobe TRAJAN.
Should not have
• flashy colors

```html
<!DOCTYPE html>
<html lang="fr">
<head>
<meta charset="utf-8">
<title>Prestige Aubergerie Lyon — Brochure</title>
<link href="https://fonts.googleapis.com/css2?family=Abril+Fatface&family=Josefin+Sans:wght@200;300;400&family=Open+Sans:wght@400;600&display=swap" rel="stylesheet">
<style>
:root{
  --bg:#e7e8ea;
  --navy:#2e3544;
  --ink:#2b3140;
  --tan:#c99a6c;
  --tan-soft:#d9b38c;
  --paper:#ffffff;
  --body:#4a4f5a;
}
*{margin:0;padding:0;box-sizing:border-box}
html,body{width:1200px;height:1000px;overflow:hidden;background:var(--bg)}
body{position:relative;font-family:"Open Sans",sans-serif;color:var(--body)}

.cover{position:absolute;left:50px;top:273px;width:355px;height:450px;background:var(--navy);box-shadow:0 2px 6px rgba(0,0,0,.18)}
.cover-brand{position:absolute;left:100px;top:205px;display:flex;align-items:center;gap:12px}
.cover-brand .mark{width:14px;height:14px;background:#cfd2d8}
.cover-brand .name{font-family:"Josefin Sans",sans-serif;font-weight:300;color:#d9dbe0;font-size:11.5px;line-height:13px;letter-spacing:.5px;text-transform:uppercase}

.spread{position:absolute;left:437px;width:710px;height:450px;background:var(--paper);box-shadow:0 2px 6px rgba(0,0,0,.15);overflow:hidden}
.spread::after{content:"";position:absolute;left:355px;top:0;width:1px;height:100%;background:rgba(0,0,0,.06)}
.spread-one{top:32px}
.spread-two{top:512px}
.page{position:absolute;top:0;width:355px;height:450px}
.page-left{left:0}
.page-right{left:355px}

.photo{position:absolute}
.photo-team{left:0;top:0;width:355px;height:273px;background:linear-gradient(160deg,#6b5a3a 0%,#3a3122 45%,#1e1b17 100%)}
.tag{position:absolute;left:101px;top:5px;width:152px;height:21px;background:var(--tan);color:#fff;font-family:"Josefin Sans",sans-serif;font-size:8px;letter-spacing:1.2px;text-align:center;line-height:22px;text-transform:uppercase}
.title-kicker{position:absolute;left:100px;top:260px;height:31px;padding:0 9px;background:var(--tan);color:#fff;font-family:"Abril Fatface",serif;font-size:27px;line-height:29px}
.title-main{position:absolute;left:78px;top:290px;color:var(--ink);font-family:"Josefin Sans",sans-serif;font-weight:200}
.title-main .le{position:absolute;left:0;top:6px;font-size:17px;font-weight:300}
.title-main .luxe{position:absolute;left:22px;top:-4px;font-size:76px;line-height:76px;letter-spacing:-2px;transform:scaleX(.84);transform-origin:left top;white-space:nowrap}
.title-main .demain{position:absolute;left:22px;top:62px;font-size:25px;letter-spacing:1px;white-space:nowrap;font-weight:300;transform:scaleX(.96);transform-origin:left top}
.title-rule{position:absolute;left:100px;top:380px;width:153px;height:1px;background:var(--tan)}
.title-en{position:absolute;left:100px;top:387px;width:170px;color:var(--tan-soft);font-family:"Josefin Sans",sans-serif;font-size:8.5px;letter-spacing:1.1px;line-height:12px;text-transform:uppercase;white-space:nowrap}
.folio{position:absolute;top:429px;font-size:5px;color:#999;letter-spacing:1px}

.text-col{position:absolute;font-size:5.1px;line-height:7.6px;text-align:justify;color:var(--body)}
.text-col p{margin-bottom:3.5px}
.col-fr{left:20px;top:168px;width:160px}
.col-en{left:198px;top:168px;width:140px}

.photo-hall{left:0;top:0;width:355px;height:450px;background:radial-gradient(ellipse at 50% 40%,#c8d6d8 0%,#6f6a55 35%,#3a2b22 70%,#1c1614 100%)}
.caption-box{position:absolute;background:var(--tan);color:#fff;font-size:4.6px;line-height:6.4px;padding:6px 6px}
.caption-box strong{display:block;font-weight:600;font-size:5px;margin-bottom:3px}
.caption-night{left:0;top:22px;width:98px;height:52px}
.headline-light{position:absolute;left:0;width:355px;text-align:center;color:#fff;font-family:"Abril Fatface",serif;font-size:29px;line-height:31px}
.headline-light.bottom{top:370px}

.photo-award{left:20px;top:20px;width:151px;height:111px;background:linear-gradient(135deg,#3a302c,#5a4a44 50%,#2b2a33)}
.caption-award{left:0;top:121px;width:130px;height:77px;padding:13px 7px 6px 7px}
.partner{position:absolute;left:134px;top:140px;width:40px;display:flex;align-items:center;gap:3px;font-family:"Open Sans",sans-serif;font-size:4.6px;font-weight:600;color:var(--ink);line-height:5.6px}
.partner .dot{flex:none;width:5px;height:5px;background:var(--ink)}
.caption-top{left:225px;top:0;width:130px;height:78px;padding:8px 7px}
.photo-group{left:183px;top:76px;width:150px;height:110px;background:linear-gradient(120deg,#2a3a3a,#7a4a42 50%,#2a2a30)}
.headline-dark{position:absolute;left:0;top:226px;width:355px;text-align:center;color:var(--ink);font-family:"Abril Fatface",serif;font-size:27px;line-height:28px}
.sub-en{position:absolute;left:0;top:296px;width:355px;text-align:center;color:var(--tan-soft);font-family:"Josefin Sans",sans-serif;font-size:8px;letter-spacing:1.8px;line-height:12px;text-transform:uppercase}
.body-fr{left:20px;top:350px;width:153px}
.body-en{left:183px;top:350px;width:153px}
</style>
</head>
<body>

<section class="cover">
  <div class="cover-brand">
    <span class="mark"></span>
    <span class="name">Prestige<br>Aubergerie<br>Lyon</span>
  </div>
</section>

<section class="spread spread-one">
  <div class="page page-left">
    <div class="photo photo-team" role="img" aria-label="Portrait of four school staff members in formal wear in a grand hotel salon"></div>
    <div class="tag">À la Prestige Aubergerie</div>
    <div class="title-kicker">inventez</div>
    <div class="title-main">
      <span class="le">LE</span>
      <span class="luxe">LUXE</span>
      <span class="demain">DE DEMAIN</span>
    </div>
    <div class="title-rule"></div>
    <div class="title-en">Invent tomorrow's luxuries<br>at the Prestige Aubergerie</div>
    <span class="folio" style="left:175px">[2]</span>
  </div>
  <div class="page page-right">
    <div class="text-col col-fr">
      <p>Depuis sa création il y a 30 ans, notre école garde le même objectif : que chaque étudiant acquière les compétences et développe les talents essentiels pour briller dans l'univers du luxe. Première école dédiée à l'hôtellerie de luxe, la Prestige Aubergerie délivre un Bachelor et un Master of Science in International Tourism and Hospitality Management, deux grades universitaires anglais.</p>
      <p>Cette combinaison du luxe à la française et du management anglo-saxon donne toutes les clés à nos étudiants pour s'assurer une place privilégiée dans l'univers du luxe en France et à l'international.</p>
      <p>Grâce à l'excellence académique de nos programmes, la dimension internationale de nos formations et l'immersion professionnelle à travers des stages dans les plus prestigieux hôtels du monde, tous nos diplômés sont assurés de faire carrière dans le secteur de leur choix à un poste stratégique. La moitié d'entre eux signent un CDI avant même la fin de leur dernier stage.</p>
    </div>
    <div class="text-col col-en">
      <p>Since its foundation 30 years ago, our school has had only one objective: that each student acquires the skills and develops the essential talents they require to shine within the luxury sector. The Prestige Aubergerie is the first Higher Education establishment dedicated to luxury hotel training: we offer a Bachelor's and a Master's degree in International Tourism and Hospitality Management.</p>
      <p>This combination of French-style luxury and Anglo-Saxon management gives our students the key elements they need to ensure a privileged position within the luxury industry both in France and internationally.</p>
      <p>The academic excellence of our programmes, the international dimension of our training and our professional work placements at the most prestigious hotels in the world all ensure that our graduates are certain to secure a career in a strategic role in the luxury sector. Half of our students sign a permanent contract before they even finish their final work placement.</p>
    </div>
    <span class="folio" style="left:176px">[3]</span>
  </div>
</section>

<section class="spread spread-two">
  <div class="page page-left">
    <div class="photo photo-hall" role="img" aria-label="Grand palace hotel lobby with crystal chandelier, glass roof and red lounge seating"></div>
    <div class="caption-box caption-night">
      <strong>Une nuit au Palace<br>A night at the Palace</strong>
      Une expérience unique au palace Maison Orsane, pour vivre le service d'exception de l'intérieur.
    </div>
    <div class="headline-light bottom">Vivez l'expérience<br>du luxe…</div>
  </div>
  <div class="page page-right">
    <div class="photo photo-award" role="img" aria-label="Student receiving a certificate from a hotel director"></div>
    <div class="caption-box caption-award">
      Le palace Maison Orsane, partenaire de longue date, accueille nos étudiants pour une remise de prix. The palace welcomes our students for a prize ceremony with its manager.
    </div>
    <div class="partner"><span class="dot"></span><span>Maison Orsane<br>Lyon</span></div>
    <div class="caption-box caption-top">
      Les étudiants en Bachelor dans les salons du palace pour une journée d'immersion. Bachelor students spend a day inside the palace and gain a first concrete experience in one of the finest hotels in Lyon.
    </div>
    <div class="photo photo-group" role="img" aria-label="Group of students in suits posing in a hotel salon"></div>
    <div class="headline-dark">… et devenez-en le<br>meilleur Ambassadeur</div>
    <div class="sub-en">Experience the luxury<br>sector and become<br>its finest ambassador</div>
    <div class="text-col body-fr">
      <p>Au sein de la Prestige Aubergerie, vous suivez un programme consacré au luxe pour vous imprégner au mieux de cet univers hors du commun et pouvoir en appréhender tous les aspects. La posture, le protocole, la gestuelle, l'apparence : c'est en suivant des cours en immersion et en vivant des expériences concrètes dans les plus beaux hôtels que vous en mesurerez toute l'importance. Avec « Une nuit au Palace », « Luxury Shopping », « Goûtez le Luxe », « Afternoon tea » et tant d'autres activités, vous découvrez, du point de vue d'un client, le faste et l'art de vivre à la française.</p>
    </div>
    <div class="text-col body-en">
      <p>Studying at the Prestige Aubergerie, you will follow a programme that is 100% focused on luxury so that you can really soak up this extraordinary world and get an understanding of every aspect. By following our immersive classes and gaining concrete experience in the most incredible hotels, you'll learn just how important luxury attitude is. With "A night at the Palace", "Luxury Shopping", "A Taste of Luxury", "Afternoon tea" and a whole host of other activities, you will get a taste of what life is like for luxury guests and the French art of living.</p>
    </div>
  </div>
</section>

</body>
</html>
```